CV brochure for Top Management Position

I need me to introduce myself a brochure design for a CV brochure in. So sort of a resume in booklet format. The design should be serious for a convey on the other, the viewer that I stand for the new world of digitization. The brochure is intended to convey that I am a "Digital Leader". With the brochure boards, boards of directors and decision makers of enterprises should pay attention to my person. It must not be a 0815 design of the rod. The design should already be addressed with the front page of the topic Digital Leader, since the front page usually is the decisive criterion whether to continue dealing with the person or not. I am now CIO (IT manager) and wants to move with the brochure myself from this technique corner out and thus make it interesting for other positions. The positions are in absolute top management, the board, management, supervisory anchored and deal primarily with the digital transformation and the new digital world. So should appear with security on the front page a concise picture of me. but I am also very open to any alternative proposal brochure. Here you can see my current CV with picture and the basic content. The brochure is even more responsive to the social skills and not only to the technical projects implemented as before.

Target Market(s)

Top management, CxO level, supervisory boards, large companies, large Mittlestandsunternehmen

Industry/Entity Type

Management

Font styles to use
Serif
Sans Serif

Requirements
Must have
• see description
Nice to have
• see description
Should not have
• see description

```html
<!DOCTYPE html>
<html lang="de">
<head>
<meta charset="utf-8">
<title>Lebenslauf-Broschüre – Dr. Lukas Brenner</title>
<link href="https://fonts.googleapis.com/css2?family=Open+Sans:wght@400;600;700&family=Archivo:wght@400;800&display=swap" rel="stylesheet">
<style>
  :root{
    --bg:#8ea7bd;
    --paper:#ffffff;
    --paper-soft:#f1f2f3;
    --ink:#222222;
    --accent-red:#7a1a17;
    --accent-blue:#1d2fb0;
    --muted:#555b62;
  }
  *{box-sizing:border-box;margin:0;padding:0}
  html,body{width:1200px;height:826px;overflow:hidden}
  body{background:var(--bg);font-family:"Open Sans",Arial,sans-serif;color:var(--ink);position:relative}

  .spread{position:absolute;display:flex;box-shadow:0 10px 30px rgba(30,50,70,.25);background:var(--paper)}
  .spread--inside{left:40px;top:28px;width:1120px;height:390px}
  .spread--cover{left:240px;top:440px;width:720px;height:362px}
  .panel{flex:1;position:relative;overflow:hidden}
  .panel + .panel{border-left:1px solid #e4e6e8}

  .photo{position:absolute;inset:0}
  .photo--writing{background:linear-gradient(160deg,#6d6450 0%,#b9aa92 40%,#e9e6e0 75%,#d8d9dc 100%)}
  .photo--tablet{background:linear-gradient(150deg,#4a3a2c 0%,#2d2a28 30%,#c9cfd6 55%,#e8ebef 80%,#3b2d22 100%)}
  .photo--meeting{background:linear-gradient(135deg,#35506f 0%,#6f89a6 35%,#d9dfe6 65%,#8fa1b4 100%)}

  .text-panel{padding:30px 26px 24px}
  .heading{font-family:"Open Sans",Arial,sans-serif;font-weight:600;font-size:21px;color:var(--accent-red);margin-bottom:16px}
  .check-list{list-style:none}
  .check-list li{display:flex;gap:7px;font-size:9.2px;line-height:1.4;margin-bottom:10px;text-align:justify}
  .check-list--dense li{margin-bottom:7px;font-size:8.6px}
  .check-list svg{flex:0 0 9px;width:9px;height:9px;margin-top:2px}
  .check-list strong{font-weight:700}

  .cover-panel{background:linear-gradient(90deg,var(--paper-soft),#ffffff 60%,#e7ecf2);padding:26px 28px}
  .name{font-family:"Archivo",Arial,sans-serif;font-weight:800;font-size:20px;letter-spacing:1.5px;color:var(--accent-blue)}
  .role{font-family:"Archivo",Arial,sans-serif;font-size:12.5px;letter-spacing:1.6px;color:var(--accent-blue);line-height:1.2}
  .portrait{display:block;margin:16px auto 18px;width:130px;height:82px;border-radius:50%;background:radial-gradient(circle at 45% 40%,#b89c7c,#6d6a5c 60%,#3e4a52)}
  .contact-grid{display:grid;grid-template-columns:1fr 1fr;gap:10px 18px}
  .contact-item{text-align:center}
  .contact-item dt{font-family:"Archivo",Arial,sans-serif;font-weight:800;font-size:9px;letter-spacing:.8px;color:var(--muted)}
  .contact-item dd{font-size:7.5px;color:var(--muted);letter-spacing:.3px}
</style>
</head>
<body>
<svg width="0" height="0" style="position:absolute" aria-hidden="true">
  <symbol id="tick" viewBox="0 0 10 10">
    <rect x="0.6" y="0.6" width="8.8" height="8.8" fill="none" stroke="#222" stroke-width="1"/>
    <path d="M2.2 5.2 L4.2 7.2 L8.2 2.4" fill="none" stroke="#222" stroke-width="1.3"/>
  </symbol>
</svg>

<section class="spread spread--inside">
  <article class="panel text-panel overview">
    <h2 class="heading">Auf einen Blick</h2>
    <ul class="check-list">
      <li><svg><use href="#tick"/></svg><span>Kommunikationsstarke Führungspersönlichkeit mit mehrjähriger Erfahrung in Leitungsfunktionen im IT-Bereich, aktuell Chief Information Officer (CIO) und Chief Digital Officer (CDO)</span></li>
      <li><svg><use href="#tick"/></svg><span>Umfangreiche Fachexpertise in: Konzeption und Weiterentwicklung von IT-Unternehmensstrategien | Effizienzsteigerung im IT-Bereich | Optimierung der IT-Service-Strukturen | Planung und Durchführung konzernweiter IT-Programme</span></li>
      <li><svg><use href="#tick"/></svg><span>Experte auf dem Gebiet der Transformation von Unternehmen in die digitale Welt (Industrie 4.0) | Etablierung der IT als Business Enabler</span></li>
      <li><svg><use href="#tick"/></svg><span>Führung von 75 MA + ca. 20 (weltweit und extern), davon 4 Führungskräfte | Budget i.H.v. 22 Mio. € p.a.</span></li>
      <li><svg><use href="#tick"/></svg><span>Wissensmanager mit interkultureller Kompetenz, breitem Technologieverständnis sowie ausgeprägter Durchsetzungs- und Teamfähigkeit</span></li>
      <li><svg><use href="#tick"/></svg><span>umsetzungsstark | lösungsorientiert | unternehmerisch | visionär</span></li>
    </ul>
  </article>
  <div class="panel">
    <div class="photo photo--writing" role="img" aria-label="Foto: Hand mit Stift schreibt in ein Notizbuch neben einer Laptop-Tastatur"></div>
  </div>
  <div class="panel">
    <div class="photo photo--tablet" role="img" aria-label="Foto: Tablet auf einem Holztisch mit Web-Analyse-Dashboard"></div>
  </div>
  <article class="panel text-panel experience">
    <h2 class="heading">Berufliche Erfahrungen</h2>
    <ul class="check-list check-list--dense">
      <li><svg><use href="#tick"/></svg><span><strong>Falkner Gruppe</strong> | Reutlingen | www.falkner-gruppe.de<br>Weltweiter Hersteller von zerspanenden Präzisionswerkzeugen | 7.000 MA weltweit in ca. 50 Ländern | 900 Mio. € Umsatz</span></li>
      <li><svg><use href="#tick"/></svg><span><strong>Chief Information Officer/ Chief Digital Officer</strong><br>Verantwortung der operativen sowie strategischen IT weltweit</span></li>
      <li><svg><use href="#tick"/></svg><span>Verantwortung der digitalen Transformation der Firma weltweit, Umsetzung der Vision Falkner 2020</span></li>
      <li><svg><use href="#tick"/></svg><span>Aufbau einer IT-Strategie in Abstimmung mit Geschäftsführung und Eigentümer</span></li>
      <li><svg><use href="#tick"/></svg><span>Entwicklung und Umsetzung einer ERP-Roadmap 2020, inkl. Einführung ERP-Suite Nova, Einführung Nova One in ca. 40 Tochtergesellschaften weltweit</span></li>
      <li><svg><use href="#tick"/></svg><span>Aufbau eines IT-Risikomanagementsystems in Zusammenhang mit IT-GRC-Strukturen</span></li>
      <li><svg><use href="#tick"/></svg><span>Definition einer zentralen e-Business Multichannel Architektur, Aufbau einer IT-Leistungsrechnung sowie eines IT-Controllings, Aufbau zweier IT Hubs in Asien und Amerika</span></li>
      <li><svg><use href="#tick"/></svg><span>Neuausrichtung der gesamten IT-Infrastruktur (Migration von Orion zu Vega)</span></li>
      <li><svg><use href="#tick"/></svg><span>Etablierung einer IT-Projektmethodik</span></li>
    </ul>
  </article>
</section>

<section class="spread spread--cover">
  <div class="panel">
    <div class="photo photo--meeting" role="img" aria-label="Foto: Geschäftsmann im Anzug erklärt mit offener Hand an einem Schreibtisch mit Laptop"></div>
  </div>
  <header class="panel cover-panel">
    <h1 class="name">Dr. Lukas Brenner</h1>
    <p class="role">Chief Information Officer (CIO)<br>Ph.D. Wirtschaftsinformatik</p>
    <span class="portrait" role="img" aria-label="Porträtfoto des Bewerbers"></span>
    <dl class="contact-grid">
      <div class="contact-item"><dt>Adresse</dt><dd>Lindenweg 8, 10115 Berlin</dd></div>
      <div class="contact-item"><dt>Mobil</dt><dd>+ 49 (0) 170 00 0000 00</dd></div>
      <div class="contact-item"><dt>Geburtsdaten</dt><dd>29. März 1978 in Konstanz</dd></div>
      <div class="contact-item"><dt>E-Mail</dt><dd>mail@beispiel.de</dd></div>
      <div class="contact-item"><dt>Familienstand</dt><dd>verheiratet | 2 Kinder</dd></div>
      <div class="contact-item"><dt>Profil</dt><dd>https://profil.beispiel.de/</dd></div>
    </dl>
  </header>
</section>
</body>
</html>
```